Real estate agent : TJ Property

I have done the attached logo designed by your company .
My business card description as below:
Name : Daniel Ruiz
Mobile: 0491570156
Email : danielr@tjpropertyhq.net.au
Sales & Property Management

```html
<!DOCTYPE html>
<html lang="en">
<head>
<meta charset="utf-8">
<title>TJ Property – Business Card</title>
<link rel="stylesheet" href="https://fonts.googleapis.com/css2?family=Montserrat:wght@400;500;700;800&display=swap">
<style>
  :root {
    --backdrop: #e7e4df;
    --card-dark: #2d2d2d;
    --card-light: #ffffff;
    --ink: #2b2b2b;
    --gold: #a8823e;
    --gold-rule: #c9b27f;
    --white: #ffffff;
  }
  * { margin: 0; padding: 0; box-sizing: border-box; }
  html, body {
    width: 900px; height: 1200px; overflow: hidden;
    background: var(--backdrop);
    font-family: "Montserrat", sans-serif;
  }
  .canvas { position: relative; width: 900px; height: 1200px; }
  .card {
    position: absolute; left: 80px; width: 742px; height: 442px;
    border-radius: 30px;
    box-shadow: 0 6px 14px rgba(0,0,0,0.25);
  }
  .card-front { top: 130px; background: var(--card-dark); }
  .card-back { top: 637px; background: var(--card-light); }

  .brand-name {
    position: absolute; font-weight: 800; text-transform: uppercase;
    line-height: 0.95; letter-spacing: 1px;
  }
  .brand-name .brand-initials { display: block; }
  .card-front .brand-name { right: 42px; top: 272px; color: var(--white); text-align: right; }
  .card-front .brand-initials { font-size: 92px; }
  .card-front .brand-word { font-size: 30px; }
  .card-back .brand-name { left: 42px; top: 98px; color: var(--ink); }
  .card-back .brand-initials { font-size: 96px; }
  .card-back .brand-word { font-size: 32px; }

  .holder { position: absolute; right: 46px; top: 202px; text-align: right; }
  .holder-name { font-size: 26px; font-weight: 700; color: var(--gold); line-height: 1.2; }
  .holder-title { font-size: 16px; font-weight: 400; color: var(--ink); }
  .divider {
    position: absolute; left: 42px; right: 46px; top: 259px;
    height: 1.5px; background: var(--gold-rule);
  }
  .contacts { position: absolute; left: 42px; top: 270px; list-style: none; }
  .contacts li {
    display: flex; align-items: center; gap: 12px;
    font-size: 15.5px; color: var(--ink); height: 24.5px;
  }
  .contacts svg { width: 16px; height: 16px; fill: var(--gold); flex: none; }
</style>
</head>
<body>
<div class="canvas">
  <section class="card card-front">
    <div class="brand-name"><span class="brand-initials">TJ</span><span class="brand-word">Property</span></div>
  </section>

  <section class="card card-back">
    <div class="brand-name"><span class="brand-initials">TJ</span><span class="brand-word">Property</span></div>
    <div class="holder">
      <p class="holder-name">Daniel Ruiz</p>
      <p class="holder-title">Real Estate Broker</p>
    </div>
    <div class="divider"></div>
    <ul class="contacts">
      <li><svg viewBox="0 0 24 24"><path d="M6.6 10.8a15.1 15.1 0 0 0 6.6 6.6l2.2-2.2a1 1 0 0 1 1-.25 11.4 11.4 0 0 0 3.6.57 1 1 0 0 1 1 1V20a1 1 0 0 1-1 1A17 17 0 0 1 3 4a1 1 0 0 1 1-1h3.5a1 1 0 0 1 1 1c0 1.25.2 2.45.57 3.57a1 1 0 0 1-.25 1z"/></svg>0491570156</li>
      <li><svg viewBox="0 0 24 24"><path d="M2 5h20v2l-10 6L2 7z M2 9l10 6 10-6v10H2z"/></svg>danielr@tjpropertyhq.net.au</li>
      <li><svg viewBox="0 0 24 24"><circle cx="12" cy="12" r="10"/></svg>www.tjpropertyhq.net.au</li>
    </ul>
  </section>
</div>
</body>
</html>
```